Spectacular Business Card Design for AI SAAS Plattform called Pathleap.ai

Hi Creators
I need an outstanding new Design for my business card.
I run an AI automated Saas Plattform Called Pathleap.ai

Front side:
Logo
Slogan: DIY Business Development & Social Media Management
Data:
Name: Markus Velbringer - CEO / Founder
email: m.velbringer@pathleap-example.ai
mobile: +43 699 82 37 915

Company name:
Pathleap FlexCo

Backside:

What we stand for Slogan:
Vertrauen in KI-Technologie, getragen von menschlicher Vision: Dein Sprung nach vorn!
+ a fancy design what captures our core competencies - AI automisations, Social Media Management, Business development
(dont know if its too much, but AI and social media should be )

pls find attached the logo and the old design

Industry/Entity Type

AI automations for marketing and business development

Contact Information for Business Card

Front side: Logo Slogan: DIY Business Development & Social Media Management Data: Name: Markus Velbringer - CEO / Founder email: m.velbringer@pathleap-example.ai mobile: +43 699 82 37 915 Company name: Pathleap FlexCo Backside: What we stand for Slogan: Vertrauen in KI-Technologie, getragen von menschlicher Vision: Dein Sprung nach vorn!

Font styles to use
Serif
Sans Serif

Requirements
Nice to have
• a fancy design on the backside, a fancy design what captures our core competencies - AI automisations, Social Media Management, Business development

```html
<!DOCTYPE html>
<html lang="de">
<head>
<meta charset="utf-8">
<title>Pathleap.ai – Business Card</title>
<link rel="stylesheet" href="https://fonts.googleapis.com/css2?family=Roboto:wght@400;500;700&display=swap">
<style>
  :root {
    --stage: #1b1d20;
    --teal: #0897b6;
    --teal-deep: #0a6ea6;
    --orange: #f3962c;
    --blue-name: #0d6a9c;
    --ink: #3a3a3a;
    --rule: #4a4a4a;
    --white: #ffffff;
  }
  * { box-sizing: border-box; margin: 0; padding: 0; }
  html, body { width: 1200px; height: 840px; overflow: hidden; }
  body {
    background: var(--stage);
    font-family: "Roboto", Arial, sans-serif;
    position: relative;
  }
  .card {
    position: absolute;
    left: 290px;
    width: 620px;
    height: 354px;
    border-radius: 22px;
    overflow: hidden;
  }

  /* Back side */
  .card--back {
    top: 48px;
    background: linear-gradient(35deg, var(--teal-deep) 0%, var(--teal) 45%, #099ab7 100%);
    color: var(--white);
    display: flex;
    flex-direction: column;
    align-items: center;
    justify-content: center;
    text-align: center;
    padding: 0 40px;
  }
  .brand {
    display: flex;
    align-items: center;
    gap: 12px;
    font-weight: 700;
    letter-spacing: 0.5px;
  }
  .brand__mark { width: 22px; height: 22px; background: var(--orange); }
  .card--back .brand { font-size: 50px; margin-bottom: 26px; }
  .slogan { font-size: 16px; line-height: 1.3; font-weight: 400; }
  .slogan + .slogan { margin-top: 10px; }

  /* Front side */
  .card--front {
    top: 438px;
    background: var(--white);
    border-bottom: 6px solid var(--teal);
  }
  .card--front .brand {
    position: absolute;
    right: 44px;
    top: 54px;
    font-size: 50px;
    color: var(--teal);
  }
  .person {
    position: absolute;
    left: 44px;
    top: 160px;
  }
  .person__name { font-size: 23px; font-weight: 700; letter-spacing: 0.3px; }
  .person__first { color: var(--blue-name); }
  .person__last { color: var(--orange); }
  .person__role { font-size: 18px; color: var(--ink); margin-top: 4px; }
  .divider {
    position: absolute;
    left: 44px;
    right: 44px;
    top: 232px;
    height: 1px;
    background: var(--rule);
  }
  .contact {
    position: absolute;
    left: 44px;
    top: 250px;
    list-style: none;
    font-size: 17px;
    color: var(--ink);
  }
  .contact li { display: flex; align-items: center; gap: 10px; margin-bottom: 8px; }
  .contact svg { width: 18px; height: 18px; flex: none; }
  .tagline {
    position: absolute;
    right: 44px;
    top: 250px;
    text-align: right;
    font-size: 16px;
    line-height: 1.35;
    color: var(--ink);
  }
</style>
</head>
<body>

  <section class="card card--back" aria-label="Back side">
    <div class="brand"><span class="brand__mark"></span>Pathleap</div>
    <p class="slogan">Vertrauen in KI-Technologie, getragen von menschlicher Vision:<br>Dein Sprung nach vorn!</p>
    <p class="slogan">+ a fancy design what captures our core competencies -<br>AI automisations, Social Media Management, Business development</p>
  </section>

  <section class="card card--front" aria-label="Front side">
    <div class="brand"><span class="brand__mark"></span>Pathleap</div>

    <div class="person">
      <p class="person__name"><span class="person__first">MARKUS</span> <span class="person__last">VELBRINGER</span></p>
      <p class="person__role">CEO / Founder</p>
    </div>

    <div class="divider"></div>

    <ul class="contact">
      <li>
        <svg viewBox="0 0 24 24" aria-hidden="true"><path fill="#f3962c" d="M6.6 10.8a15.1 15.1 0 0 0 6.6 6.6l2.2-2.2c.3-.3.7-.4 1-.2 1.1.4 2.3.6 3.6.6.6 0 1 .4 1 1V20c0 .6-.4 1-1 1A17 17 0 0 1 3 4c0-.6.4-1 1-1h3.5c.6 0 1 .4 1 1 0 1.3.2 2.5.6 3.6.1.3 0 .7-.2 1z"/></svg>
        +43 699 82 37 915
      </li>
      <li>
        <svg viewBox="0 0 24 24" aria-hidden="true"><path fill="#f3962c" d="M3 5h18a1 1 0 0 1 1 1v12a1 1 0 0 1-1 1H3a1 1 0 0 1-1-1V6a1 1 0 0 1 1-1zm9 7.5L20 7H4z"/></svg>
        m.velbringer@pathleap-example.ai
      </li>
    </ul>

    <p class="tagline">DIY Business Development<br>&amp; Social Media Management</p>
  </section>

</body>
</html>
```